Business Card - Rebranding for Consulting Firm

We are renaming and rebranding our consulting firm and need to raise the level of quality of our cards as part of that effort. We consult to leading high tech, life science and other innovation sector companies.

Need a two-sided business card design.

Side 1: (a) Company logo (b) tag line: Optimize Your Investment in Talent (c) Name (d) Title (e) Phone 1: Office (f) Phone 2: Mobile (g) email: person@HollowmereAdvisory.com

Side 2: Two lines of text: (a) Growth is Imperative. Change is Constant. Talent Executes Strategy. (b) We help you excel at all three.

Target Market(s)

Business and human resources executives and senior managers

Industry/Entity Type

Management Consulting

Contact Information for Business Card

Font styles to use
Sans Serif

Requirements
Must have
• clean, not too busy, but with a bit of creativity. Stick to the colors used in the attached logo
• appeal to high tech, life science companies
Nice to have
• prefer white background

```html
<!DOCTYPE html>
<html lang="en">
<head>
<meta charset="utf-8">
<title>Hollowmere Advisory – Business Card</title>
<link rel="stylesheet" href="https://fonts.googleapis.com/css2?family=Source+Sans+3:wght@400;600;700&display=swap">
<style>
  :root {
    --backdrop: #1c1c1c;
    --card-white: #ffffff;
    --brand-blue: #1a66a8;
    --brand-cyan: #009fdf;
    --brand-deep: #0a6aaa;
    --ink: #1e1e1e;
    --ink-soft: #3c3c3c;
    --on-blue: #ffffff;
  }
  * { margin: 0; padding: 0; box-sizing: border-box; }
  html, body {
    width: 1200px; height: 900px; overflow: hidden;
    background: var(--backdrop);
    font-family: "Source Sans 3", "Segoe UI", sans-serif;
  }
  .stage { position: relative; width: 1200px; height: 900px; }
  .card {
    position: absolute; top: 170px; width: 347px; height: 561px;
    text-align: center;
  }
  .card--front { left: 259px; background: var(--card-white); }
  .card--back {
    left: 631px;
    background: linear-gradient(160deg, var(--brand-cyan) 0%, var(--brand-deep) 45%, #0b74b8 75%, var(--brand-cyan) 100%);
    color: var(--on-blue);
  }
  .accent-band {
    position: absolute; left: 102px; width: 143px; height: 30px;
    background: linear-gradient(180deg, #1c8fd4 0%, var(--brand-cyan) 100%);
  }
  .accent-band--top { top: 0; }
  .accent-band--bottom { bottom: 0; height: 28px; }
  .brand-name {
    position: absolute; left: 0; right: 0; top: 128px;
    font-size: 34px; font-weight: 600; color: var(--brand-blue);
    line-height: 1.1;
  }
  .holder-name {
    position: absolute; left: 0; right: 0; top: 295px;
    font-size: 23px; font-weight: 700; color: var(--brand-blue);
  }
  .holder-title {
    position: absolute; left: 0; right: 0; top: 324px;
    font-size: 15px; color: var(--ink-soft);
  }
  .contact-list {
    position: absolute; left: 0; right: 0; top: 362px;
    list-style: none; font-size: 14.5px; color: var(--ink-soft); line-height: 21.5px;
  }
  .contact-list b { color: var(--brand-blue); font-weight: 700; }
  .website {
    position: absolute; left: 0; right: 0; top: 441px;
    font-size: 15.5px; font-weight: 700; color: var(--brand-blue);
  }
  .tagline {
    position: absolute; left: 0; right: 0; top: 482px;
    font-size: 19px; color: var(--ink);
  }
  .back-brand {
    position: absolute; left: 0; right: 0; top: 258px;
    font-size: 34px; font-weight: 600; color: var(--on-blue);
  }
  .back-sweep { position: absolute; inset: 0; }
  .credo {
    position: absolute; left: 0; right: 0; top: 374px;
    font-size: 21px; line-height: 34.5px; color: var(--on-blue);
  }
</style>
</head>
<body>
<main class="stage">
  <section class="card card--front" aria-label="Card front">
    <div class="accent-band accent-band--top"></div>
    <p class="brand-name">Hollowmere<br>Advisory</p>
    <h1 class="holder-name">DANIEL REYES</h1>
    <p class="holder-title">Managing Director</p>
    <ul class="contact-list">
      <li><b>P:</b> 555-014-2290</li>
      <li><b>M:</b>&nbsp; 555-014-2290</li>
      <li><b>E:</b> person@HollowmereAdvisory.com</li>
    </ul>
    <p class="website">www.HollowmereAdvisory.com</p>
    <p class="tagline">Optimize Your Investment in Talent</p>
    <div class="accent-band accent-band--bottom"></div>
  </section>

  <section class="card card--back" aria-label="Card back">
    <svg class="back-sweep" width="347" height="561" viewBox="0 0 347 561" aria-hidden="true">
      <polygon points="0,480 347,310 347,330 0,505" fill="#ffffff" opacity="0.12"/>
    </svg>
    <p class="back-brand">Hollowmere Advisory</p>
    <p class="credo">Growth is Imperative.<br>Change is Constant.<br>Talent Executes Strategy<br>We help you excel at all three</p>
  </section>
</main>
</body>
</html>
```